bluecastle aquatics of northeast florida business card

I need a new attractive business card. I am planning on printing on very thick rounded corner stock and having painted edges. We are a swimming pool remodel, repair, and service company in north florida. Our current logo is red, white, and blue. It doesn't necessarily have to stay that way, I am open to other ideas. It will need to contain my name, work and cell numbers, email, website, and my contractor license number.

Target Market(s)

High end residential and commercial clients

Industry/Entity Type

Business

Contact Information for Business Card

Company name, employee name and title, work and cell phone numbers, email and website, and Contractor number.

our work scope should be on card somewhere: remodel ~ repair ~ service

logo or slight variation of logo also. (not necessarily set on keeping exact logo)

Colors

Designer to choose colors to be used in the design.

Requirements
Nice to have
• We deal with water so I think some sort of water element or just a color similar to pool water would be nice to integrate into design.

```html
<!DOCTYPE html>
<html lang="en">
<head>
<meta charset="utf-8">
<title>Bluecastle Aquatics – Business Card</title>
<link href="https://fonts.googleapis.com/css2?family=Montserrat:wght@400;500;700&display=swap" rel="stylesheet">
<style>
  :root {
    --backdrop: #e9e8e6;
    --card: #ffffff;
    --ink: #16161c;
    --pool: #44d7e3;
    --shadow: rgba(0,0,0,0.14);
  }
  * { margin: 0; padding: 0; box-sizing: border-box; }
  html, body { width: 806px; height: 1200px; overflow: hidden; }
  body {
    background: var(--backdrop);
    font-family: "Montserrat", sans-serif;
    color: var(--ink);
    position: relative;
  }
  .card {
    position: absolute;
    left: 24px;
    width: 758px;
    height: 432px;
    background: var(--card);
    border-radius: 28px;
    overflow: hidden;
    box-shadow: 0 6px 18px var(--shadow);
  }
  .card--front { top: 137px; }
  .card--back { top: 595px; }
  .water-lines {
    position: absolute;
    top: 0; left: 0;
    width: 758px; height: 432px;
  }
  .water-lines rect { fill: var(--pool); }
  .brand-dot {
    position: absolute;
    left: 86px; top: 44px;
    width: 86px; height: 86px;
    border-radius: 50%;
    background: var(--pool);
  }
  .brand-name {
    position: absolute;
    left: 88px; top: 152px;
    font-weight: 700;
    font-size: 44px;
    line-height: 74px;
    letter-spacing: 0.26em;
    text-transform: uppercase;
  }
  .brand-region {
    position: absolute;
    left: 90px; top: 318px;
    font-weight: 500;
    font-size: 19px;
    letter-spacing: 0.16em;
    text-transform: uppercase;
  }
  .brand-scope {
    position: absolute;
    left: 90px; top: 360px;
    font-weight: 500;
    font-size: 14px;
    letter-spacing: 0.2em;
    text-transform: uppercase;
    color: var(--pool);
  }
  .person-name {
    position: absolute;
    left: 46px; top: 44px;
    font-weight: 700;
    font-size: 50px;
    line-height: 56px;
    letter-spacing: 0.08em;
    text-transform: uppercase;
  }
  .person-title {
    position: absolute;
    left: 48px; top: 170px;
    font-size: 17px;
    letter-spacing: 0.14em;
  }
  .contact {
    position: absolute;
    left: 48px; top: 262px;
    list-style: none;
    font-size: 17px;
    line-height: 28px;
    letter-spacing: 0.1em;
  }
</style>
</head>
<body>

<section class="card card--front">
  <svg class="water-lines" viewBox="0 0 758 432" aria-hidden="true">
    <rect x="600" y="8" width="170" height="14" rx="7"/>
    <rect x="660" y="36" width="110" height="14" rx="7"/>
    <rect x="690" y="64" width="80" height="14" rx="7"/>
    <rect x="636" y="92" width="134" height="14" rx="7"/>
    <rect x="604" y="120" width="166" height="14" rx="7"/>
    <rect x="680" y="148" width="90" height="14" rx="7"/>
    <rect x="650" y="176" width="120" height="14" rx="7"/>
    <rect x="700" y="204" width="70" height="14" rx="7"/>
    <rect x="620" y="232" width="150" height="14" rx="7"/>
    <rect x="672" y="260" width="98" height="14" rx="7"/>
    <rect x="604" y="288" width="166" height="14" rx="7"/>
    <rect x="690" y="316" width="80" height="14" rx="7"/>
    <rect x="640" y="344" width="130" height="14" rx="7"/>
    <rect x="664" y="372" width="106" height="14" rx="7"/>
    <rect x="612" y="400" width="158" height="14" rx="7"/>
  </svg>
  <div class="brand-dot"></div>
  <h1 class="brand-name">Bluecastle<br>Aquatics</h1>
  <p class="brand-region">of Northeast Florida</p>
  <p class="brand-scope">remodel ~ repair ~ service</p>
</section>

<section class="card card--back">
  <svg class="water-lines" viewBox="0 0 758 432" aria-hidden="true">
    <rect x="580" y="12" width="190" height="14" rx="7"/>
    <rect x="640" y="40" width="130" height="14" rx="7"/>
    <rect x="690" y="68" width="80" height="14" rx="7"/>
    <rect x="610" y="96" width="160" height="14" rx="7"/>
    <rect x="700" y="124" width="70" height="14" rx="7"/>
    <rect x="660" y="152" width="110" height="14" rx="7"/>
    <rect x="596" y="180" width="174" height="14" rx="7"/>
    <rect x="680" y="208" width="90" height="14" rx="7"/>
    <rect x="630" y="236" width="140" height="14" rx="7"/>
    <rect x="700" y="264" width="70" height="14" rx="7"/>
    <rect x="610" y="292" width="160" height="14" rx="7"/>
    <rect x="666" y="320" width="104" height="14" rx="7"/>
    <rect x="640" y="348" width="130" height="14" rx="7"/>
    <rect x="690" y="376" width="80" height="14" rx="7"/>
    <rect x="600" y="404" width="170" height="14" rx="7"/>
  </svg>
  <h2 class="person-name">Ray<br>Holden</h2>
  <p class="person-title">manager</p>
  <ul class="contact">
    <li>P 904 555 012</li>
    <li>M 904-555-019</li>
    <li>ray@bluecastlepools.com</li>
    <li>bluecastlepools.com</li>
    <li>Licence No. CPC 148 207</li>
  </ul>
</section>

</body>
</html>
```